Printed Promo Flyer for new pet business

We need a double sided flyer design as per the given example flyer, just better looking and more fun.Flyers will need to be printed.Flyer size approx 10.5cm x 15cm. The text will need to be amended slightly afterwards to be more fun unless you can create a new tone of voice as well (should sound fun like breezy do it) Look and Feel: emotional, fun, loving, professional
See attached files.

Target Market(s)

Pet owners in the UK who want the convenience of getting their pets parasite treatment delivered to their door without the need of having to run to the vet or store for purchase

Industry/Entity Type

Pet Care

Colors
00a990
6b449b

Requirements
Must have
• all the content context as given in the example flyer.
Nice to have
• Tone of voice can be changed to be more fun (using Breezy as a guide)

```html
<!DOCTYPE html>
<html lang="en">
<head>
<meta charset="utf-8">
<title>Pawly Box – Flyer Front and Back</title>
<link rel="stylesheet" href="https://fonts.googleapis.com/css2?family=Raleway:wght@400;500;600;700&family=Roboto+Condensed:wght@300;400&display=swap">
<style>
  :root{
    --teal:#00a990;
    --teal-deep:#009a8c;
    --purple:#6b449b;
    --purple-deep:#5e2d87;
    --white:#ffffff;
    --ink:#222222;
    --stage:#e6e6e6;
    --cream:#ecd7ae;
    --ginger:#e9a05a;
    --golden:#e2c795;
    --scrubs:#a98ad6;
  }
  *{box-sizing:border-box;margin:0;padding:0}
  html,body{width:1200px;height:1200px;overflow:hidden}
  body{background:var(--stage);position:relative;font-family:"Raleway",sans-serif}

  .flyer{position:absolute;top:221px;width:530px;height:758px;background:var(--white);overflow:hidden;
    box-shadow:6px 8px 14px rgba(0,0,0,.28)}
  .flyer--front{left:47px}
  .flyer--back{left:623px;font-family:"Roboto Condensed",sans-serif}

  /* FRONT */
  .front__box{position:absolute;left:55px;top:220px;width:420px;height:330px;
    background:linear-gradient(90deg,#9a9a9a 0%,#e6e6e6 5%,#f8f8f8 50%,#e6e6e6 95%,#9a9a9a 100%)}
  .front__photo{position:absolute;left:70px;top:30px;width:410px;height:250px;border-radius:46% 46% 12% 12% / 60% 60% 10% 10%;
    background:
      radial-gradient(ellipse 30% 45% at 78% 58%,var(--ginger) 0%,rgba(233,160,90,.85) 55%,rgba(233,160,90,0) 100%),
      radial-gradient(ellipse 45% 60% at 34% 48%,#f1e0bd 0%,var(--cream) 55%,rgba(236,215,174,0) 100%)}
  .brand{color:var(--purple-deep);font-family:"Raleway",sans-serif;font-weight:700;text-align:center;letter-spacing:2px}
  .front__brand{position:absolute;left:0;width:530px;top:410px;font-size:44px}
  .front__brand .dot{display:inline-block;width:14px;height:14px;border-radius:50%;background:var(--teal);margin-right:12px;vertical-align:middle}
  .front__curve{position:absolute;left:0;top:500px;width:530px}
  .front__teal{position:absolute;left:0;top:545px;width:530px;height:122px;background:var(--teal)}
  .front__tagline{position:absolute;left:0;width:530px;top:544px;text-align:center;color:var(--white);
    font-size:15px;letter-spacing:3.4px;font-weight:500}
  .front__headline{position:absolute;left:0;width:530px;text-align:center;color:var(--white);font-weight:600;line-height:1}
  .front__headline small{font-size:24px;font-weight:500;margin-right:10px}
  .front__headline--one{top:572px;font-size:42px}
  .front__headline--two{top:615px;font-size:42px}
  .front__purple{position:absolute;left:0;top:666px;width:530px;height:92px;background:var(--purple-deep);color:var(--white);text-align:center}
  .front__offer{margin-top:18px;font-size:15.5px;font-weight:500}
  .front__url{margin-top:8px;font-size:14px;letter-spacing:6px;font-weight:500}

  /* BACK */
  .back__photo{position:absolute;left:0;top:0;width:530px;height:372px;
    background:
      radial-gradient(ellipse 24% 38% at 82% 26%,var(--scrubs) 0%,rgba(169,138,214,.8) 60%,rgba(169,138,214,0) 100%),
      radial-gradient(ellipse 55% 26% at 52% 80%,var(--golden) 0%,rgba(226,199,149,.85) 60%,rgba(226,199,149,0) 100%),
      linear-gradient(90deg,#e9e3d4 0%,#f1ede4 45%,#f5f3ef 100%)}
  .back__table{position:absolute;left:0;top:330px;width:530px;height:42px;background:linear-gradient(180deg,rgba(255,255,255,0),#e6ebf1)}
  .back__brand{position:absolute;left:58px;top:270px;width:220px;font-size:30px;text-align:center}
  .back__brand .dot{display:inline-block;width:10px;height:10px;border-radius:50%;background:var(--teal);margin-right:8px;vertical-align:middle}
  .back__why{position:absolute;left:44px;top:340px;font-size:27px;color:var(--purple-deep);font-weight:400}
  .why{position:absolute;left:0;top:372px;width:530px;height:173px;background:var(--purple-deep)}
  .why__item{position:absolute;display:flex;align-items:flex-start;color:var(--white)}
  .why__icon{width:62px;height:62px;border-radius:50%;background:var(--teal);flex:none;display:flex;align-items:center;justify-content:center}
  .why__text{margin-left:12px;font-size:12px;line-height:15px;font-weight:300}
  .why__title{font-size:14.5px;font-weight:400;line-height:17px}
  .why__item--care{left:28px;top:18px}
  .why__item--post{left:266px;top:18px}
  .why__item--time{left:28px;top:90px}
  .why__item--cost{left:266px;top:90px}
  .why__item--post .why__text,.why__item--cost .why__text{padding-top:8px}
  .why__item--time .why__text{padding-top:8px}
  .how{position:absolute;left:0;top:545px;width:530px;height:145px}
  .how__title{position:absolute;left:39px;top:14px;font-size:27px;color:var(--purple-deep);font-weight:400}
  .how__list{position:absolute;left:52px;top:56px;list-style:none;font-size:12.5px;color:var(--ink)}
  .how__list li{height:19.5px;display:flex;align-items:center}
  .how__list svg{margin-right:8px}
  .how__pets{position:absolute;left:292px;top:6px;width:222px;height:92px;border-radius:40% 40% 8px 8px / 30% 30% 8px 8px;
    background:linear-gradient(90deg,#3a3330 0%,#8a6a4c 18%,#d49a5a 38%,#8b5a34 56%,#c88d55 72%,#ece6de 86%,#3b3634 100%)}
  .back__rule{position:absolute;left:0;top:690px;width:530px;height:6px;background:var(--purple-deep)}
  .back__footer{position:absolute;left:0;top:696px;width:530px;height:62px;background:var(--teal);
    color:var(--white);text-align:center;font-family:"Raleway",sans-serif;font-size:16px;font-weight:600;letter-spacing:5px;padding-top:18px}
</style>
</head>
<body>

<section class="flyer flyer--front">
  <div class="front__box"></div>
  <div class="front__photo" role="img" aria-label="Photo of a fluffy cream puppy and a ginger kitten peeking over a white box"></div>
  <div class="brand front__brand"><span class="dot"></span>PAWLY BOX</div>
  <svg class="front__curve" width="530" height="60" viewBox="0 0 530 60" aria-hidden="true">
    <path d="M0 48 Q265 -10 530 48 L530 60 L0 60 Z" fill="var(--teal)"/>
  </svg>
  <div class="front__teal"></div>
  <p class="front__tagline">THE BEST PROTECTION AND CARE</p>
  <p class="front__headline front__headline--one"><small>FOR</small>YOUR PET</p>
  <p class="front__headline front__headline--two"><small>WITH</small>PAWLY BOX</p>
  <div class="front__purple">
    <p class="front__offer">Flea &amp; Tick Treatment Delivered To Your Door Every Month.</p>
    <p class="front__url">www.pawlybox.co.uk</p>
  </div>
</section>

<section class="flyer flyer--back">
  <div class="back__photo" role="img" aria-label="Photo of a smiling vet in purple scrubs with a golden retriever on an exam table"></div>
  <div class="back__table"></div>
  <div class="brand back__brand"><span class="dot"></span>PAWLY BOX</div>
  <h2 class="back__why">Why Us</h2>

  <div class="why">
    <div class="why__item why__item--care">
      <div class="why__icon">
        <svg width="40" height="40" viewBox="0 0 40 40" aria-hidden="true" fill="none" stroke="var(--purple-deep)" stroke-width="2" stroke-linecap="round">
          <ellipse cx="20" cy="23" rx="7" ry="9" fill="var(--purple-deep)"/>
          <circle cx="20" cy="12" r="3.5" fill="var(--purple-deep)"/>
          <path d="M13 18 L6 14 M13 23 L5 23 M13 28 L6 33 M27 18 L34 14 M27 23 L35 23 M27 28 L34 33 M18 9 L15 5 M22 9 L25 5"/>
        </svg>
      </div>
      <div class="why__text"><p class="why__title">PROTECTION &amp; CARE</p>Protection against all major<br>parasites to avoid putting your<br>pet and your family at risk</div>
    </div>
    <div class="why__item why__item--post">
      <div class="why__icon">
        <svg width="40" height="30" viewBox="0 0 40 30" aria-hidden="true" fill="none" stroke="var(--purple-deep)" stroke-width="2" stroke-linejoin="round">
          <rect x="2" y="3" width="36" height="24"/>
          <path d="M2 3 L20 17 L38 3 M2 27 L15 13 M38 27 L25 13"/>
        </svg>
      </div>
      <div class="why__text"><p class="why__title">CONVENIENT</p>Delivered directly to<br>Your letter box</div>
    </div>
    <div class="why__item why__item--time">
      <div class="why__icon">
        <svg width="44" height="44" viewBox="0 0 44 44" aria-hidden="true" fill="none" stroke="var(--purple-deep)" stroke-width="2.5" stroke-linecap="round">
          <circle cx="22" cy="22" r="18"/>
          <path d="M22 10 L22 22 L15 30"/>
        </svg>
      </div>
      <div class="why__text"><p class="why__title">IN TIME</p>Never having to remember<br>When to treat your pet</div>
    </div>
    <div class="why__item why__item--cost">
      <div class="why__icon">
        <svg width="30" height="42" viewBox="0 0 30 42" aria-hidden="true">
          <text x="15" y="35" text-anchor="middle" font-family="Raleway, sans-serif" font-weight="700" font-size="38" fill="var(--purple-deep)">$</text>
        </svg>
      </div>
      <div class="why__text"><p class="why__title">LOW COST</p>All the high end, trusted brands<br>But cheaper than the vet</div>
    </div>
  </div>

  <div class="how">
    <h2 class="how__title">How it works</h2>
    <div class="how__pets" role="img" aria-label="Photo of a row of assorted dog breeds sitting together"></div>
    <ul class="how__list">
      <li><svg width="14" height="12" viewBox="0 0 14 12" aria-hidden="true"><path d="M1 6 L5 10 L13 1" fill="none" stroke="var(--teal)" stroke-width="2.6"/></svg>Select which pet the treatment is for</li>
      <li><svg width="14" height="12" viewBox="0 0 14 12" aria-hidden="true"><path d="M1 6 L5 10 L13 1" fill="none" stroke="var(--teal)" stroke-width="2.6"/></svg>Choose your treatment type</li>
      <li><svg width="14" height="12" viewBox="0 0 14 12" aria-hidden="true"><path d="M1 6 L5 10 L13 1" fill="none" stroke="var(--teal)" stroke-width="2.6"/></svg>Select your preferred brand</li>
      <li><svg width="14" height="12" viewBox="0 0 14 12" aria-hidden="true"><path d="M1 6 L5 10 L13 1" fill="none" stroke="var(--teal)" stroke-width="2.6"/></svg>Choose between 1, 3, 6 or 12 Months treatment box</li>
    </ul>
  </div>

  <div class="back__rule"></div>
  <div class="back__footer">www.pawlybox.co.uk</div>
</section>

</body>
</html>
```